Cover for "ROOTED! The skill and rhythm of guiding teams through calm and delight"

My first book for a global audience of modern performance leaders needs its cover!
I am an international executive coach and I've developed a new approach to replace classic Performance Management with a natural, sustainable approach fit for human beings :) My first book is about this approach and serves two purposes: helping leaders and sparking their curiosity to learn more, and positioning myself as a thought leader in the field.
The book is built on personal experience; it is both professional and personal ("From me to You"), and I'd like to position it beyond classic categorisation.
Its cover should communicate humanness, naturalness, ease and joy, within an unmistakably business-y context. I would like to see designs that use the color yellow (but not sure it communicates the right things).
Updates

Target Market(s)

Leaders who aspire to have a positive impact and deliver results in a meaningful way

Industry/Entity Type

Consulting & Executive Coaching - Trusted Advisor

Font styles to use
Other font styles liked:
• Helvetica Neue

Colors
0094D4
00A9DD
6FCCEA
C7EBF8
E9F6FB
FFC000
F8CF3A
FAE287
FDF2CF
FEFAEE
EE7325
F08F49
F5BC92
FAE3D3
FDF4ED

Requirements
Must have
• A both-and feeling to it (see description), e.g., masculine AND feminine, business AND humanness. Power with, not power over...
Should not have
• Too much "bling" - no classic status symbol business success language

```html
<!DOCTYPE html>
<html lang="en">
<head>
<meta charset="utf-8">
<title>ROOTED! — Book Cover</title>
<link rel="stylesheet" href="https://fonts.googleapis.com/css2?family=Arimo:wght@400;700&display=swap">
<style>
  :root {
    --orange-deep: #ee7325;
    --orange: #f39a1c;
    --amber: #ffc000;
    --yellow-glow: #ffe45a;
    --yellow-core: #fff3a0;
    --white: #ffffff;
    --ink: #2e2210;
  }
  html, body {
    margin: 0;
    padding: 0;
    width: 805px;
    height: 1200px;
    overflow: hidden;
  }
  .cover {
    position: relative;
    width: 805px;
    height: 1200px;
    overflow: hidden;
    font-family: "Arimo", "Helvetica Neue", Arial, sans-serif;
    background: var(--orange);
  }
  .cover-glow {
    position: absolute;
    inset: 0;
    width: 805px;
    height: 1200px;
  }
  .author {
    position: absolute;
    top: 38px;
    left: 0;
    width: 805px;
    text-align: center;
    margin: 0;
    color: var(--white);
    font-weight: 700;
    font-size: 30px;
    letter-spacing: 0.3px;
    transform: translateX(-160px);
  }
  .title {
    position: absolute;
    top: 355px;
    left: 0;
    width: 805px;
    margin: 0;
    text-align: center;
    color: var(--white);
    font-weight: 700;
    font-size: 168px;
    line-height: 1;
    letter-spacing: 2px;
  }
  .subtitle {
    position: absolute;
    top: 548px;
    left: 0;
    width: 805px;
    margin: 0;
    text-align: center;
    color: var(--white);
    font-weight: 400;
    font-size: 38px;
    line-height: 56px;
    text-transform: uppercase;
    letter-spacing: 0.5px;
  }
  .tagline {
    position: absolute;
    top: 1012px;
    left: 60px;
    width: 600px;
    margin: 0;
    text-align: center;
    color: var(--ink);
    font-weight: 700;
    font-size: 27px;
    line-height: 45px;
  }
</style>
</head>
<body>
  <main class="cover">
    <svg class="cover-glow" viewBox="0 0 805 1200" aria-hidden="true">
      <defs>
        <linearGradient id="base-tone" x1="0" y1="0" x2="0" y2="1">
          <stop offset="0" stop-color="#f39a1c"/>
          <stop offset="0.2" stop-color="#f5a21e"/>
          <stop offset="0.45" stop-color="#ffc000"/>
          <stop offset="0.75" stop-color="#f8a41f"/>
          <stop offset="1" stop-color="#f08f2a"/>
        </linearGradient>
        <radialGradient id="sun-glow" cx="0.5" cy="0.5" r="0.5">
          <stop offset="0" stop-color="#fff6b0"/>
          <stop offset="0.35" stop-color="#ffe45a"/>
          <stop offset="0.75" stop-color="#ffc000" stop-opacity="0.6"/>
          <stop offset="1" stop-color="#ffc000" stop-opacity="0"/>
        </radialGradient>
        <linearGradient id="horizon-edge" x1="0" y1="0" x2="0" y2="1">
          <stop offset="0" stop-color="#ffd65a" stop-opacity="0.9"/>
          <stop offset="1" stop-color="#ffd65a" stop-opacity="0"/>
        </linearGradient>
      </defs>
      <rect width="805" height="1200" fill="url(#base-tone)"/>
      <ellipse cx="402" cy="560" rx="620" ry="360" fill="url(#sun-glow)"/>
      <path d="M -60 300 Q 402 180 865 300 L 865 360 Q 402 240 -60 360 Z" fill="url(#horizon-edge)" opacity="0.6"/>
      <path d="M -60 300 Q 402 180 865 300" fill="none" stroke="#ffdf7a" stroke-width="3" opacity="0.8"/>
    </svg>

    <p class="author">Author Name</p>
    <h1 class="title">ROOTED!</h1>
    <p class="subtitle">The skill and rhythm of<br>guiding teams through<br>calm and delight</p>
    <p class="tagline">Performance Management with a Natural<br>and Sustainable approach<br>fit for Human Beings</p>
  </main>
</body>
</html>
```